International Legal Service Company needs Letterhead Design

Put my new Logo into Letterhead Design, using updated telephone number, e-mail address and website. Current letterhead and updated information which i want you to include my new letterhead attached herewith. Of course, my new Logo attached herein. Also, you can use slogan "Total Legal Outsourcing Solutions For Multinational Businesses"

It Company

```html
<!DOCTYPE html>
<html lang="en">
<head>
<meta charset="utf-8">
<title>Meridian Counsel Group Inc — Letterhead</title>
<link rel="stylesheet" href="https://fonts.googleapis.com/css2?family=Fira+Sans:wght@400;600&family=Fira+Sans+Condensed:wght@600&display=swap">
<style>
  :root {
    --backdrop: #a9a9a9;
    --paper: #ffffff;
    --ink: #222222;
    --brand-navy: #1d3a7a;
    --brand-blue: #2f63b8;
    --rule: #333333;
    --signature-tint: #dfe6f3;
  }
  * { margin: 0; padding: 0; box-sizing: border-box; }
  html, body {
    width: 1012px; height: 1200px; overflow: hidden;
    background: var(--backdrop);
  }
  .letterhead {
    position: absolute; left: 266px; top: 178px;
    width: 536px; height: 756px;
    background: var(--paper);
    color: var(--ink);
    font-family: "Fira Sans", sans-serif;
  }
  .brand { position: absolute; left: 27px; top: 17px; display: flex; align-items: center; gap: 12px; }
  .brand-mark { width: 72px; height: 72px; border-radius: 50%; background: var(--brand-blue); }
  .brand-name {
    font-weight: 600; font-size: 20px; line-height: 1.15;
    color: var(--brand-navy); margin-top: 6px;
  }
  .header-contact {
    position: absolute; left: 356px; top: 56px;
    font-family: "Fira Sans Condensed", sans-serif; font-weight: 600;
    font-size: 9px; line-height: 12px; color: #111;
  }
  .header-rule {
    position: absolute; left: 27px; top: 110px; width: 482px;
    border-top: 1px solid var(--rule);
  }
  .salutation { position: absolute; left: 53px; top: 168px; font-size: 18px; font-weight: 400; }
  .letter-body { position: absolute; left: 53px; top: 224px; width: 437px; }
  .letter-body p {
    font-size: 10.4px; line-height: 15.8px; text-align: justify;
    margin-bottom: 16px; hyphens: auto;
  }
  .closing { position: absolute; right: 48px; top: 526px; font-size: 10.4px; }
  .signature {
    position: absolute; left: 402px; top: 557px; width: 90px; height: 38px;
    background: var(--signature-tint); border-radius: 4px;
  }
  .footer-contact {
    position: absolute; left: 27px; top: 720px;
    display: flex; align-items: center;
    font-family: "Fira Sans Condensed", sans-serif; font-weight: 600;
    font-size: 9px; color: #111;
  }
  .footer-divider { width: 1px; height: 18px; background: var(--rule); margin: 0 7px; }
  .footer-mark {
    position: absolute; left: 438px; top: 676px;
    width: 56px; height: 56px; border-radius: 50%; background: var(--brand-blue);
  }
</style>
</head>
<body>
  <main class="letterhead">
    <header>
      <div class="brand">
        <div class="brand-mark"></div>
        <div class="brand-name">Meridian Counsel<br>Group Inc</div>
      </div>
      <div class="header-contact">
        <div>E-Mail: contact@meridiancounsel.example</div>
        <div>Website: http://meridiancounsel.example.com</div>
      </div>
      <div class="header-rule"></div>
    </header>

    <h1 class="salutation">Dear Mr. Smith,</h1>

    <section class="letter-body">
      <p>Lorem ipsum dolor sit amet, consectetur adipiscing elit. Donec orci purus, luctus vitae dignissim eu, iaculis sed purus. Vivamus faucibus, ipsum nec aliquet viverra, leo mauris condimentum ligula, sit amet sagittis enim ligula quis arcu. Nam egestas tortor id nisi porttitor mattis. In tortor ante, ultricies in suscipit a, tempus non massa. Vivamus et auctor mi. Fusce vel massa nulla. Phasellus nec eros mauris, et scelerisque orci.</p>
      <p>Donec malesuada orci vitae nulla accumsan porta a id massa. Quisque accumsan iaculis magna sit amet fringilla. Maecenas consequat, magna eget tincidunt semper, odio nibh rutrum mi, id feugiat ante nisi eu risus. Vestibulum nunc orci, rhoncus a placerat in, ultricies in mi. Cras mattis varius eros, vel fringilla nisi suscipit eget. Quisque scelerisque sagittis nulla at porttitor.</p>
      <p>Sed id augue vitae urna euismod commodo aliquet a quam. Pellentesque arcu velit, cursus et malesuada ut, consequat et diam. Nullam erat sem, rhoncus id ullamcorper vitae, rhoncus et arcu. In ultricies ultricies nulla, ut rutrum nisi iaculis at. Donec eu magna a metus ornare faucibus. Fusce aliquet faucibus ultricies. Morbi semper, est id tincidunt gravida, sem arcu adipiscing lacus, ac bibendum nulla leo eu purus. Quisque nec diam sed risus consectetur a ccumsan quis quis nibh. Vestibulum id purus lorem.</p>
    </section>

    <p class="closing">Sincerely,</p>
    <div class="signature" role="img" aria-label="Handwritten signature of John Doe"></div>

    <footer>
      <div class="footer-contact">
        <span>1480 Harbor Point Drive Suite 300 Lakeview, MD 20900</span>
        <span class="footer-divider"></span>
        <span>Tel: 240-555-0142 Fax: 240-555-0178</span>
      </div>
      <div class="footer-mark"></div>
    </footer>
  </main>
</body>
</html>
```